Simple, High-Class Web Design Wanted - Motivational Speakers Site

1. Full Brief/Request & Specs outlined on following video -
http://clipvane-recorder.com/watch/tbWrkLmQyP

2. Use colours, images as you feel suits objective (we are happy to pay up to US$30 for any good images but must have licence/permission).

3. Layout probably similar to existing site - www.podiumvoicehub.com.au / http://podiumvoicehub.com.au/contact.php

4. Must Be Able to Coded for MOBILE-FRIENDLINESS & WordPress friendly Ideal.

5. This is the first, small job of many we/graphic design jobs. If suits, winning designer may be offered all future work direct.

Thanks & look forward to your design. Glen.

Target Market(s)

corporates - high end

Number of Pages Required

2 page

Font styles to use
Sans Serif

Requirements
Must have
• Classy professional look
Nice to have
• all in Video in brief
Should not have
• too many images / new images I haven't approved

```html
<!DOCTYPE html>
<html lang="en">
<head>
<meta charset="utf-8">
<title>Podium Voice Hub</title>
<link href="https://fonts.googleapis.com/css2?family=Open+Sans:wght@400;600;700&display=swap" rel="stylesheet">
<style>
:root{
  --red:#c33a1c;
  --teal:#3fc6bd;
  --mint:#e8f8f6;
  --ink:#2b2b2b;
  --muted:#7a7a7a;
  --band:#dde2e8;
  --footer:#313439;
  --footer-deep:#25272b;
  --white:#ffffff;
}
*{margin:0;padding:0;box-sizing:border-box}
html,body{width:726px;height:1200px;overflow:hidden}
body{font-family:"Open Sans",Arial,sans-serif;color:var(--ink);background:var(--white);position:relative}
.nav{height:68px;display:flex;justify-content:center;align-items:center;gap:26px;font-size:11px;font-weight:600;letter-spacing:.5px}
.nav a{color:var(--ink);text-decoration:none}
.hero{position:relative;height:262px;overflow:hidden}
.hero-photo{position:absolute;inset:0;background:linear-gradient(90deg,#cbbfae 0%,#b9a690 45%,#8c7a66 75%,#6b5a4a 100%)}
.hero-crowd{position:absolute;left:0;right:0;bottom:0;height:80px;background:linear-gradient(180deg,rgba(60,45,35,0) 0%,rgba(60,45,35,.55) 100%)}
.hero-speaker{position:absolute;right:40px;top:10px;width:190px;height:252px;background:linear-gradient(180deg,#3a3a40 0%,#1f2024 100%);border-radius:90px 90px 0 0;opacity:.85}
.hero-copy{position:absolute;left:104px;top:30px;color:var(--white)}
.hero h1{font-size:27px;line-height:1.25;font-weight:700;width:390px;text-shadow:0 1px 2px rgba(0,0,0,.3)}
.hero .tag{font-size:13px;font-weight:600;margin-top:14px}
.watch{margin-top:22px;display:inline-flex;align-items:center;gap:12px;background:var(--white);color:var(--ink);font-size:17px;padding:6px 10px 6px 16px;border-radius:3px}
.watch svg{display:block}
.hero .note{font-size:10px;margin-top:8px;width:170px;line-height:1.35}
.cta-tab{position:absolute;left:300px;top:330px;width:126px;height:34px;background:var(--red);color:var(--white);font-size:12px;font-weight:600;display:flex;justify-content:center;align-items:center;clip-path:polygon(0 0,100% 0,92% 100%,8% 100%)}
.cta-chev{position:absolute;left:355px;top:366px}
.about{text-align:center;padding-top:62px}
.about h2{font-size:15px;font-weight:700}
.about p{font-size:9.5px;color:var(--muted);line-height:1.6;width:420px;margin:14px auto 0}
.about p b{color:var(--red);font-weight:600}
.how{position:absolute;top:552px;left:0;width:726px;height:262px;background:var(--mint);text-align:center}
.how h2{font-size:21px;font-weight:400;margin-top:28px}
.how .sub{font-size:9.5px;color:var(--muted);margin-top:4px}
.steps{display:flex;justify-content:center;gap:50px;margin-top:26px}
.step{width:150px}
.step .icon{width:72px;height:72px;border-radius:50%;background:var(--teal);margin:0 auto;display:flex;justify-content:center;align-items:center}
.step h3{font-size:11px;color:var(--red);font-weight:700;margin-top:14px}
.step p{font-size:9.5px;color:var(--muted);line-height:1.45;margin-top:4px}
.contact{position:absolute;top:822px;left:0;width:726px;height:172px;background:var(--band);overflow:hidden}
.contact-photo{position:absolute;right:60px;top:0;width:200px;height:172px;background:linear-gradient(180deg,#c99a72 0%,#e2c4a8 55%,#f2e6dc 100%);border-radius:100px 100px 0 0}
.contact-copy{position:absolute;left:104px;top:34px}
.contact h2{font-size:23px;font-weight:400}
.contact .sub{font-size:13px;margin-top:8px}
.btn{margin-top:16px;display:inline-flex;align-items:center;gap:14px;background:var(--red);color:var(--white);font-size:12px;padding:8px 16px}
.footer{position:absolute;top:994px;left:0;width:726px;height:172px;background:var(--footer);color:#c9cbcf;display:flex;gap:70px;padding:26px 0 0 104px}
.footer h4{font-size:8px;font-weight:700;letter-spacing:.5px;color:var(--white);margin-bottom:10px}
.footer li{list-style:none;font-size:8px;line-height:2.1;display:flex;align-items:center;gap:6px}
.footer .dot{width:10px;height:10px;border-radius:50%;border:1px solid #8a8d92}
.news p{font-size:8px;line-height:1.5;width:150px}
.news .field{display:flex;margin-top:8px}
.news .field span{width:122px;height:18px;background:var(--white);font-size:7px;color:#999;padding:4px 6px}
.news .field i{width:18px;height:18px;background:var(--teal)}
.social{display:flex;gap:8px;margin-top:26px;margin-left:60px}
.social span{width:10px;height:10px;border-radius:50%;background:#8a8d92}
.bottom{position:absolute;top:1166px;left:0;width:726px;height:34px;background:var(--footer-deep);font-size:8px;color:#8a8d92;padding:12px 0 0 104px}
</style>
</head>
<body>
<nav class="nav"><a>HOME</a><a>HOW IT WORKS</a><a>CONTACT US</a></nav>

<section class="hero">
  <div class="hero-photo" role="img" aria-label="Photo of a speaker in a suit with a microphone addressing a conference audience"></div>
  <div class="hero-crowd"></div>
  <div class="hero-speaker"></div>
  <div class="hero-copy">
    <h1>Find The Perfect Speaker For Your Next Event Here ...</h1>
    <div class="tag">Free Industry Service</div>
    <div class="watch">Watch Video
      <svg width="24" height="24" viewBox="0 0 24 24"><circle cx="12" cy="12" r="11" fill="none" stroke="var(--red)" stroke-width="2"/><path d="M9.5 7.5v9l7-4.5z" fill="var(--red)"/></svg>
    </div>
    <p class="note">Some text explaining the benefit in short can come here</p>
  </div>
</section>

<div class="cta-tab">Get In Touch</div>
<svg class="cta-chev" width="16" height="14" viewBox="0 0 16 14"><path d="M2 2l6 5 6-5M2 7l6 5 6-5" fill="none" stroke="var(--red)" stroke-width="1.6"/></svg>

<section class="about">
  <h2>About Podium Voice Hub</h2>
  <p>Podium Voice Hub is a <b>free industry service</b> designed to help people looking for speakers save precious time and frustration in finding the most suitable speaker for their needs.</p>
  <p>Suggestions are given by Australian conference speaker Glen Harlow, who has presented around Australia for a number of years and is familiar with many of our top professional speakers, MC's as well as the leading speaker bureaus.</p>
</section>

<section class="how">
  <h2>How it works</h2>
  <div class="sub">Some lines we share how the process works</div>
  <div class="steps">
    <div class="step">
      <div class="icon"><svg width="30" height="30" viewBox="0 0 30 30"><path d="M4 15l22-10-8 22-4-9z" fill="none" stroke="#fff" stroke-width="2" stroke-linejoin="round"/></svg></div>
      <h3>Send us your requirements</h3>
      <p>Using some dummy text for now which we will replace once you send us the content</p>
    </div>
    <div class="step">
      <div class="icon"><svg width="30" height="30" viewBox="0 0 30 30"><circle cx="10" cy="10" r="4" fill="none" stroke="#fff" stroke-width="2"/><circle cx="20" cy="10" r="4" fill="none" stroke="#fff" stroke-width="2"/><path d="M3 24c1-5 4-7 7-7s6 2 7 7M13 24c1-5 4-7 7-7s6 2 7 7" fill="none" stroke="#fff" stroke-width="2"/></svg></div>
      <h3>Our experts analyze them</h3>
      <p>Using some dummy text for now which we will replace once you send us the content</p>
    </div>
    <div class="step">
      <div class="icon"><svg width="30" height="30" viewBox="0 0 30 30"><rect x="7" y="4" width="16" height="22" rx="2" fill="none" stroke="#fff" stroke-width="2"/><path d="M11 15l3 3 6-6" fill="none" stroke="#fff" stroke-width="2"/></svg></div>
      <h3>Find a perfect solution</h3>
      <p>Using some dummy text for now which we will replace once you send us the content</p>
    </div>
  </div>
</section>

<section class="contact">
  <div class="contact-photo" role="img" aria-label="Photo of a smiling woman representing the support team"></div>
  <div class="contact-copy">
    <h2>Get in touch with us</h2>
    <div class="sub">Our experts will help you get the best speakers</div>
    <div class="btn">Get In Touch With Us Now
      <svg width="8" height="12" viewBox="0 0 8 12"><path d="M1 1l5 5-5 5" fill="none" stroke="#fff" stroke-width="2"/></svg>
    </div>
  </div>
</section>

<footer class="footer">
  <div>
    <h4>CONTACT DETAILS</h4>
    <ul>
      <li><span class="dot"></span>+61 02 5550 1842</li>
      <li><span class="dot"></span>hello@podiumvoicehub.com.au</li>
      <li><span class="dot"></span>Podium Voice Hub</li>
    </ul>
  </div>
  <div>
    <h4>COMPANY</h4>
    <ul><li>Home</li><li>How it works</li><li>Contact</li></ul>
  </div>
  <div class="news">
    <h4>NEWSLETTER SIGN UP</h4>
    <p>Get our latest news and speaker tips sent straight to your inbox each month.</p>
    <div class="field"><span>Email address</span><i></i></div>
    <div class="social"><span></span><span></span><span></span></div>
  </div>
</footer>
<div class="bottom">© 2016 Podium Voice Hub</div>
</body>
</html>
```